Business Card for Industrial Distributor

We need a business card design for an industrial distributor. We sell machine parts for the manufacturing and oil industry. We would like the cards to look clean and modern but with a touch of industry.

Our colors are blue/white.

Please feel free to visit our website www.korvanlineusa.com

Target Market(s)

mexican manufacturers in the automobile/aerospace industry

Industry/Entity Type

Industrial

Colors
ffffff
0555a3

```html
<!DOCTYPE html>
<html lang="en">
<head>
<meta charset="utf-8">
<title>Korvanline Business Card</title>
<link href="https://fonts.googleapis.com/css2?family=Montserrat:wght@400;600;800&display=swap" rel="stylesheet">
<style>
  :root {
    --navy: #2a3591;
    --band-blue: #0a7bc4;
    --title-blue: #1e88d0;
    --white: #ffffff;
    --stage: #e9ecef;
    --card-shadow: rgba(20, 30, 60, 0.18);
  }
  * { margin: 0; padding: 0; box-sizing: border-box; }
  html, body {
    width: 1200px; height: 900px; overflow: hidden;
    background: var(--stage);
    font-family: "Montserrat", sans-serif;
  }
  .stage {
    width: 1200px; height: 900px;
    display: flex; flex-direction: column;
    align-items: center; justify-content: center; gap: 40px;
  }
  .card {
    position: relative;
    width: 700px; height: 400px;
    border-radius: 22px;
    background: var(--white);
    overflow: hidden;
    box-shadow: 0 10px 30px var(--card-shadow);
  }

  /* Front */
  .front-brand {
    position: absolute; left: 50px; top: 130px;
    display: flex; align-items: center; gap: 22px;
  }
  .brand-dot {
    width: 100px; height: 100px; border-radius: 50%;
    background: var(--navy);
  }
  .brand-name {
    font-weight: 800; color: var(--navy);
    font-size: 76px; letter-spacing: -1px; line-height: 1;
  }
  .front-web {
    position: absolute; left: 0; right: 0; bottom: 70px;
    text-align: center; color: var(--navy);
    font-size: 20px; font-weight: 400; letter-spacing: 0.5px;
  }
  .front-web strong { font-weight: 600; }

  /* Back */
  .back-band {
    position: absolute; left: 0; right: 0; top: 205px; bottom: 0;
    background: var(--band-blue);
  }
  .back-name {
    position: absolute; left: 34px; top: 26px;
    font-weight: 800; color: var(--navy);
    font-size: 88px; letter-spacing: -1.5px; line-height: 1;
  }
  .back-dot {
    position: absolute; right: 34px; top: 140px;
    width: 160px; height: 160px; border-radius: 50%;
    background: var(--navy);
  }
  .person { position: absolute; left: 40px; top: 140px; }
  .person-name {
    font-size: 27px; font-weight: 600; color: var(--navy); line-height: 1.1;
  }
  .person-title {
    font-size: 17px; font-weight: 400; color: var(--title-blue); margin-top: 4px;
  }
  .address {
    position: absolute; left: 70px; top: 232px;
    color: var(--white); font-size: 18px; line-height: 1.35;
  }
  .contacts {
    position: absolute; left: 70px; top: 292px;
    list-style: none; color: var(--white); font-size: 18px; line-height: 1.35;
  }
  .contacts li { display: flex; align-items: center; gap: 10px; }
  .contacts svg { width: 14px; height: 14px; flex: none; }
  .contacts strong { font-weight: 600; }
</style>
</head>
<body>
<main class="stage">
  <section class="card card-front">
    <div class="front-brand">
      <span class="brand-dot"></span>
      <span class="brand-name">Korvanline</span>
    </div>
    <p class="front-web">www.<strong>korvanlineusa</strong>.com</p>
  </section>

  <section class="card card-back">
    <div class="back-band"></div>
    <div class="back-name">Korvanline</div>
    <span class="back-dot"></span>
    <div class="person">
      <p class="person-name">Marco Delgado</p>
      <p class="person-title">Director</p>
    </div>
    <p class="address">P.O. Box 4812<br>Lansing, MI 48906</p>
    <ul class="contacts">
      <li>
        <svg viewBox="0 0 24 24" fill="#ffffff"><path d="M6.6 10.8a15 15 0 0 0 6.6 6.6l2.2-2.2c.3-.3.7-.4 1-.2 1.1.4 2.3.6 3.6.6.6 0 1 .4 1 1V20c0 .6-.4 1-1 1A17 17 0 0 1 3 4c0-.6.4-1 1-1h3.5c.6 0 1 .4 1 1 0 1.3.2 2.5.6 3.6.1.3 0 .7-.2 1z"/></svg>
        <span>+330 5812-3094</span>
      </li>
      <li>
        <svg viewBox="0 0 24 24" fill="none" stroke="#ffffff" stroke-width="2"><rect x="3" y="5" width="18" height="14" rx="1"/><path d="M3 6l9 7 9-7"/></svg>
        <span>info@korvanlineusa.com</span>
      </li>
      <li>
        <svg viewBox="0 0 24 24" fill="none" stroke="#ffffff" stroke-width="2"><circle cx="12" cy="12" r="9"/><path d="M3 12h18M12 3c3 3 3 15 0 18M12 3c-3 3-3 15 0 18"/></svg>
        <span>www.<strong>korvanlineusa</strong>.com</span>
      </li>
    </ul>
  </section>
</main>
</body>
</html>
```